Interior design service, along with home organization, packing, and staging, home and business. As well as staging in conjunction with real estate sales.

Love many of your designs and will be choosing today. To inform you of the exact details needed, the name of the company is "Flourish by Marnie T" , my phone number and e-,ail need to be included. i also need either description or some sort of bullet points that give an idea of the following:

- Interior design for home and business
- Home organization and packing
- Staging for personal and professional space
- Real estate stagingĀ 

Thank you

Target Market(s)

wide audience, but most importantly people looking for a quality service

Industry/Entity Type

Real Estate

Contact Information for Business Card

Flourish By Marnie T
Marnie Toller
(555)617-3942
mtbriar@inboxly.example

Requirements
Must have
• I'm 29 so i want my card to reflect something professional but still fresh. I don't have any specific photos or quotes that Ive included, however I like the card to reflect a personal touch, which is what I'm seeking from this service in the design of my card. Thanks!

```html
<!DOCTYPE html>
<html lang="en">
<head>
<meta charset="utf-8">
<title>Flourish by Marnie T — Business Card</title>
<link rel="stylesheet" href="https://fonts.googleapis.com/css2?family=Encode+Sans+Condensed:wght@400;500&display=swap">
<style>
  :root {
    --backdrop: #8e9da3;
    --teal: #0e5670;
    --paper: #ffffff;
    --shadow: rgba(0, 0, 0, 0.45);
  }
  html, body {
    margin: 0;
    padding: 0;
    overflow: hidden;
  }
  body {
    width: 1200px;
    height: 905px;
    background: var(--backdrop);
    position: relative;
    font-family: "Encode Sans Condensed", "Arial Narrow", sans-serif;
  }
  .card {
    position: absolute;
    box-shadow: 5px 5px 6px var(--shadow);
    overflow: hidden;
  }
  .card-front {
    left: 75px;
    top: 75px;
    width: 670px;
    height: 387px;
    background: var(--teal);
  }
  .card-back {
    left: 479px;
    top: 444px;
    width: 670px;
    height: 389px;
    background: var(--paper);
  }
  .brand {
    position: absolute;
    display: flex;
    align-items: center;
    gap: 12px;
    font-weight: 400;
    white-space: nowrap;
  }
  .brand-mark {
    width: 14px;
    height: 14px;
    background: currentColor;
  }
  .card-front .brand {
    left: 0;
    right: 0;
    top: 125px;
    justify-content: center;
    color: var(--paper);
    font-size: 24px;
    letter-spacing: 0.5px;
  }
  .front-name {
    position: absolute;
    left: 0;
    right: 0;
    top: 288px;
    margin: 0;
    text-align: center;
    color: var(--paper);
    font-size: 32px;
    font-weight: 400;
    letter-spacing: 0.6px;
  }
  .band {
    position: absolute;
    top: 135px;
    height: 117px;
    background: var(--teal);
  }
  .band-left {
    left: 0;
    width: 332px;
  }
  .band-right {
    left: 607px;
    width: 63px;
  }
  .card-back .brand {
    left: 0;
    width: 332px;
    top: 180px;
    justify-content: center;
    color: var(--paper);
    font-size: 21px;
  }
  .contact {
    position: absolute;
    left: 348px;
    top: 136px;
    color: var(--teal);
  }
  .contact-name {
    margin: 0 0 16px;
    font-size: 24px;
    font-weight: 400;
    letter-spacing: 0.4px;
  }
  .contact-line {
    margin: 0 0 12px;
    font-size: 18px;
    letter-spacing: 0.3px;
  }
  .services {
    position: absolute;
    left: 348px;
    top: 272px;
    margin: 0;
    padding: 0;
    list-style: none;
    color: var(--teal);
    font-size: 15px;
    line-height: 23px;
    letter-spacing: 0.3px;
  }
  .services li::before {
    content: "";
    display: inline-block;
    width: 6px;
    height: 6px;
    margin: 0 10px 2px 0;
    background: var(--teal);
  }
</style>
</head>
<body>
  <section class="card card-front" aria-label="Card front">
    <div class="brand"><span class="brand-mark"></span>Flourish by Marnie T</div>
    <h1 class="front-name">Marnie Toller</h1>
  </section>

  <section class="card card-back" aria-label="Card back">
    <div class="band band-left"></div>
    <div class="band band-right"></div>
    <div class="brand"><span class="brand-mark"></span>Flourish by Marnie T</div>
    <div class="contact">
      <h2 class="contact-name">Marnie Toller</h2>
      <p class="contact-line">(555)617-3942</p>
      <p class="contact-line">mtbriar@inboxly.example</p>
    </div>
    <ul class="services">
      <li>Interior design for home and business</li>
      <li>Home organization and packing</li>
      <li>Staging for personal and professional space</li>
      <li>Real estate staging</li>
    </ul>
  </section>
</body>
</html>
```